Young and modern Electrical company working in the commercial arena.

Wanting a business card design thats modern and will last. Maybe Minimalist? Happy to look at changing my logo

Target Market(s)

Builders, Project Managers

Industry/Entity Type

Electrical

Contact Information for Business Card

Name
Address
Phone number
Job title

Logo Text

our name or just the logo i'm open to ideas

Font styles to use
Sans Serif

Requirements
Nice to have
• would like to keep the purple in our current logo. it's kinda unique to our market
Should not have
• Don't want it to be to busy. simple is best i think

```html
<!DOCTYPE html>
<html lang="en">
<head>
<meta charset="utf-8">
<title>Hollis Electrical — Business Card</title>
<link rel="stylesheet" href="https://fonts.googleapis.com/css2?family=Lato:wght@400&family=Marcellus+SC&display=swap">
<style>
  :root {
    --page-bg: #e8e8eb;
    --card-dark: #3e3e3f;
    --brand-purple: #6b00c9;
    --text-light: #ffffff;
    --text-soft: #f1f1f1;
  }
  * { margin: 0; padding: 0; box-sizing: border-box; }
  html, body {
    width: 1200px;
    height: 900px;
    overflow: hidden;
    background: var(--page-bg);
  }
  .card {
    position: absolute;
    left: 150px;
    top: 171px;
    width: 900px;
    height: 558px;
    background: var(--card-dark);
    overflow: hidden;
    box-shadow: 0 10px 30px rgba(0,0,0,0.18);
  }
  .card-accent {
    position: absolute;
    inset: 0;
    width: 900px;
    height: 558px;
  }
  .brand-name {
    position: absolute;
    left: 64px;
    top: 84px;
    font-family: "Lato", sans-serif;
    font-weight: 400;
    font-size: 40px;
    line-height: 1.1;
    letter-spacing: 3px;
    color: var(--text-light);
    text-transform: uppercase;
  }
  .contact {
    position: absolute;
    left: 52px;
    top: 272px;
    color: var(--text-soft);
    font-family: "Lato", sans-serif;
  }
  .contact-name {
    font-family: "Marcellus SC", serif;
    font-size: 31px;
    line-height: 36px;
    color: var(--text-light);
    letter-spacing: 1px;
  }
  .contact-role {
    font-size: 24px;
    line-height: 30px;
    margin-bottom: 22px;
  }
  .contact-line {
    display: flex;
    align-items: center;
    gap: 8px;
    font-size: 24px;
    line-height: 34px;
  }
  .contact-line svg { width: 20px; height: 20px; fill: var(--text-light); }
  .contact-address {
    margin-top: 14px;
    font-size: 24px;
    line-height: 33px;
  }
</style>
</head>
<body>
  <div class="card">
    <svg class="card-accent" viewBox="0 0 900 558" aria-hidden="true">
      <polygon points="433,0 900,0 900,558 759,558" fill="var(--brand-purple)"/>
    </svg>

    <div class="brand-name">Hollis<br>Electrical</div>

    <div class="contact">
      <p class="contact-name">Marcus Hale</p>
      <p class="contact-role">Managing Director</p>
      <p class="contact-line">
        <svg viewBox="0 0 24 24" aria-hidden="true"><path d="M6.6 10.8a15.1 15.1 0 0 0 6.6 6.6l2.2-2.2a1 1 0 0 1 1-.25 11.4 11.4 0 0 0 3.6.57 1 1 0 0 1 1 1V20a1 1 0 0 1-1 1A17 17 0 0 1 3 4a1 1 0 0 1 1-1h3.5a1 1 0 0 1 1 1c0 1.25.2 2.45.57 3.57a1 1 0 0 1-.25 1z"/></svg>
        055-987 654 321
      </p>
      <p class="contact-line">
        <svg viewBox="0 0 24 24" aria-hidden="true"><path d="M3 5h18v14H3zM4.5 6.5 12 12l7.5-5.5v-.1h-15z" fill-rule="evenodd"/></svg>
        hello@hollisgrid.com
      </p>
      <p class="contact-address">18, Ferrow Lane,<br>Eastbrook, 60318</p>
    </div>
  </div>
</body>
</html>
```